Corvane Networks web design

Corvane is an Internet Service Provider bringing high-speed service to homes and businesses. Our principal market target is rural areas of West Michigan, but we intend to expand rapidly. We need a website to market our services, facilitate online ordering, customer support and communicate with our customers.

I will upload a draft outline of the content we hope to include in the website.

We compete directly with Halberd Communications, Lumetra, Dravix and Kelwick communications to bring Internet service to homes and businesses in our coverage area.

Our primary values include:

1. Unlike our competitors, we do not require long term contractors or service bundles; There are no termination fees, for example. All services are sold on a recurring 1-month agreement term.
2. Unlike other wireless (mobile) providers, we do not limit downloads or uploads with bit/byte buckets
3. We provide service to areas ignored by the larger carriers - Rural areas in Michigan that lack options for broadband are prime targets for Corvane to cover.
4. Unlike other wireless ISP's, we utilize licensed FCC spectrum. We do not use unlicensed/free frequencies, providing us an advantage for reliability and stability.
Updates

So many wonderful designs, thank you very much for all your hard work. We are evaluating all our favorite designs and plan to make a selection in the next 2 days. I will be in touch with you to request revisions if necessary or further refinements.  Thank you again for your efforts on this project.

Target Market(s)

Our target market is home Internet users. however, that does not mean that our users are "high tech" oriented - they are just normal mom's and pop's who buy Internet for home use. The site should be easy to navigate and communicate our message of speed, value, reliability and facilitate simple product ordering.

Industry/Entity Type

Internet

Requirements
Must have
• Our phone number should be prominently displayed 1-844-7NU-LINK
• Our logo is uploaded in the attachments.
• Design for desktop and mobile devices.
Nice to have
• The most modern of web design trends. Such as a design that facilitates parallax scrolling effects rather than lots of individual pages.
• Stock artwork communicating our values of speed and reliability.

```html
<!DOCTYPE html>
<html lang="en">
<head>
<meta charset="utf-8">
<title>Corvane Networks — 4G Wireless Internet</title>
<link rel="stylesheet" href="https://fonts.googleapis.com/css2?family=Roboto:wght@100;300;400;500;700&display=swap">
<style>
  :root {
    --brand-orange: #f47b20;
    --brand-orange-deep: #e2661a;
    --ink: #5f5f5f;
    --ink-soft: #7a7a7a;
    --ink-nav: #555555;
    --rule: #e3e3e3;
    --paper: #ffffff;
    --paper-muted: #f6f6f6;
    --hero-dark: #b5421a;
    --hero-mid: #ea7a26;
    --hero-light: #f6a35a;
    --hero-dusk: #9a8794;
  }
  * { box-sizing: border-box; margin: 0; padding: 0; }
  html, body { width: 1200px; height: 976px; overflow: hidden; background: var(--paper); }
  body { position: relative; font-family: "Roboto", Arial, sans-serif; color: var(--ink); }

  .site-header { position: absolute; left: 0; top: 0; width: 1200px; height: 173px; }
  .brand-name { position: absolute; left: 102px; top: 40px; width: 240px; font-size: 19px; line-height: 24px; font-weight: 700; color: var(--brand-orange); letter-spacing: 0.5px; text-transform: uppercase; white-space: nowrap; }
  .phone { position: absolute; left: 398px; top: 28px; display: flex; align-items: center; gap: 12px; font-size: 38px; font-weight: 300; color: var(--brand-orange); white-space: nowrap; }
  .phone svg { width: 28px; height: 28px; flex: none; }
  .search { position: absolute; left: 838px; top: 22px; width: 324px; height: 50px; display: flex; border: 1px solid #cfcfcf; border-radius: 3px; overflow: hidden; }
  .search-field { flex: 1; padding: 0 10px; display: flex; align-items: center; font-size: 17px; color: #9a9a9a; }
  .search-button { width: 52px; border-left: 1px solid #cfcfcf; background: #f2f2f2; display: flex; align-items: center; justify-content: center; }
  .header-rule { position: absolute; left: 215px; top: 106px; width: 770px; height: 1px; background: var(--rule); }
  .main-nav a { position: absolute; top: 119px; transform: translateX(-50%); font-size: 26px; font-weight: 300; color: var(--ink-nav); text-decoration: none; white-space: nowrap; }

  .tagline-band { position: absolute; left: 0; top: 173px; width: 1200px; height: 22px; background: var(--brand-orange); color: #fff; font-size: 12px; line-height: 22px; text-align: center; letter-spacing: 21px; text-transform: uppercase; padding-left: 21px; white-space: nowrap; overflow: hidden; }

  .hero { position: absolute; left: 0; top: 195px; width: 1200px; height: 358px; overflow: hidden; }
  .hero-backdrop { position: absolute; inset: 0; background: linear-gradient(100deg, var(--hero-dark) 0%, var(--hero-mid) 30%, var(--hero-light) 55%, var(--hero-mid) 78%, var(--hero-dusk) 100%); }
  .hero-title { position: absolute; left: 72px; top: 46px; font-size: 165px; font-weight: 100; color: #fff; line-height: 1; }
  .hero-signal { position: absolute; left: 310px; top: 66px; width: 132px; height: 128px; }
  .hero-subtitle { position: absolute; left: 80px; top: 210px; font-size: 50px; font-weight: 100; color: #fff; white-space: nowrap; }
  .benefits { position: absolute; left: 538px; top: 33px; width: 611px; height: 247px; background: rgba(240, 120, 40, 0.55); padding: 24px 0 0 48px; list-style: none; }
  .benefits li { position: relative; font-size: 21px; font-weight: 300; color: #fff; line-height: 36px; white-space: nowrap; }
  .benefits li::before { content: ""; position: absolute; left: -24px; top: 15px; width: 7px; height: 7px; background: #fff; }

  .plan-tabs { position: absolute; left: 82px; bottom: 0; display: flex; gap: 2px; }
  .plan-tab { width: 116px; height: 54px; display: flex; align-items: center; justify-content: center; text-align: center; font-size: 15px; line-height: 18px; color: #fff; background: rgba(230, 120, 60, 0.85); border-radius: 4px 4px 0 0; }
  .plan-tab.is-active { background: var(--paper); color: #333; }

  .plans-heading { position: absolute; left: 206px; top: 588px; font-size: 20px; font-weight: 500; color: var(--ink); }
  .plans-shadow { position: absolute; left: 90px; top: 640px; width: 1020px; height: 14px; background: radial-gradient(ellipse at top, rgba(0,0,0,0.13), rgba(0,0,0,0) 70%); }
  .purchase-band { position: absolute; left: 0; top: 860px; width: 1200px; height: 116px; background: var(--paper-muted); }
  .plan-divider { position: absolute; top: 690px; width: 1px; height: 260px; background: linear-gradient(var(--paper), #d8d8d8 30%, #d8d8d8 70%, var(--paper)); }

  .plan { position: absolute; top: 676px; width: 360px; transform: translateX(-50%); text-align: center; }
  .plan-name { font-size: 21px; font-weight: 500; color: var(--ink); line-height: 28px; }
  .plan-speed { font-size: 17px; font-weight: 400; color: var(--ink-soft); line-height: 23px; }
  .plan-price { margin-top: 4px; display: flex; justify-content: center; align-items: flex-start; color: var(--brand-orange); font-weight: 100; }
  .price-currency { font-size: 26px; font-weight: 300; margin-top: 14px; margin-right: 10px; }
  .price-whole { font-size: 92px; line-height: 1; }
  .price-cents { font-size: 26px; font-weight: 300; margin-top: 8px; margin-left: 2px; }
  .plan-fee { margin-top: 2px; font-size: 22px; font-weight: 300; color: var(--ink); }
  .buy-button { display: block; margin: 14px auto 0; width: 202px; height: 66px; line-height: 66px; background: var(--brand-orange); color: #fff; font-size: 20px; font-weight: 400; text-decoration: none; border-radius: 2px; }
</style>
</head>
<body>
  <header class="site-header">
    <div class="brand-name">Corvane Networks</div>
    <div class="phone">
      <svg viewBox="0 0 24 24" aria-hidden="true"><path fill="#f47b20" d="M6.6 10.8c1.4 2.8 3.8 5.1 6.6 6.6l2.2-2.2c.3-.3.7-.4 1-.2 1.1.4 2.3.6 3.6.6.6 0 1 .4 1 1V20c0 .6-.4 1-1 1C10.6 21 3 13.4 3 4c0-.6.4-1 1-1h3.5c.6 0 1 .4 1 1 0 1.3.2 2.5.6 3.6.1.3 0 .7-.2 1L6.6 10.8z"/></svg>
      <span>1-844-7NU-LINK</span>
    </div>
    <div class="search">
      <div class="search-field">Search</div>
      <div class="search-button">
        <svg width="22" height="22" viewBox="0 0 24 24" aria-hidden="true"><circle cx="10" cy="10" r="6.5" fill="none" stroke="#555" stroke-width="2.6"/><line x1="15" y1="15" x2="21" y2="21" stroke="#555" stroke-width="3" stroke-linecap="round"/></svg>
      </div>
    </div>
    <div class="header-rule"></div>
    <nav class="main-nav">
      <a href="#" style="left:186px">Home</a>
      <a href="#" style="left:432px">Service Plans</a>
      <a href="#" style="left:713px">Coverage Map</a>
      <a href="#" style="left:995px">About Us</a>
    </nav>
  </header>

  <div class="tagline-band">West Michigan's Best Internet Service</div>

  <section class="hero">
    <div class="hero-backdrop" role="img" aria-label="Sunset sky with glowing orange clouds"></div>
    <div class="hero-title">4G</div>
    <svg class="hero-signal" viewBox="0 0 132 128" aria-hidden="true">
      <g fill="none" stroke="#fff" stroke-linecap="round">
        <path d="M20 86 A22 22 0 0 1 42 108" stroke-width="11"/>
        <path d="M18 52 A56 56 0 0 1 76 110" stroke-width="12"/>
        <path d="M16 16 A92 92 0 0 1 112 112" stroke-width="14"/>
      </g>
    </svg>
    <div class="hero-subtitle">wireless speed</div>
    <ul class="benefits">
      <li>100% Satisfaction Guaranteed</li>
      <li>No download limits</li>
      <li>No Long Term Contracts</li>
      <li>No Phone Line or Cable TV required</li>
      <li>Fast, Superior Performance for your home and business</li>
      <li>Interference-Free FCC Licensed 4G Coverage</li>
    </ul>
    <div class="plan-tabs">
      <div class="plan-tab is-active">Home<br>Plans</div>
      <div class="plan-tab">Business<br>Plans</div>
      <div class="plan-tab">Optional<br>extras</div>
    </div>
  </section>

  <h2 class="plans-heading">Monthly plans</h2>
  <div class="plans-shadow"></div>
  <div class="purchase-band"></div>
  <div class="plan-divider" style="left:420px"></div>
  <div class="plan-divider" style="left:798px"></div>

  <article class="plan" style="left:234px">
    <h3 class="plan-name">Best Value</h3>
    <p class="plan-speed">Up to 1Mb download</p>
    <p class="plan-speed">Up to 512kbs upload</p>
    <div class="plan-price"><span class="price-currency">$</span><span class="price-whole">24</span><span class="price-cents">.99</span></div>
    <p class="plan-fee">+ $100 install fee</p>
    <a class="buy-button" href="#">Buy Now</a>
  </article>
  <article class="plan" style="left:609px">
    <h3 class="plan-name">Premium Value</h3>
    <p class="plan-speed">Up to 3Mb download</p>
    <p class="plan-speed">Up to 1Mb upload</p>
    <div class="plan-price"><span class="price-currency">$</span><span class="price-whole">44</span><span class="price-cents">.99</span></div>
    <p class="plan-fee">+ $100 install fee</p>
    <a class="buy-button" href="#">Buy Now</a>
  </article>
  <article class="plan" style="left:984px">
    <h3 class="plan-name">Unlimited</h3>
    <p class="plan-speed">Up to 10Mb download</p>
    <p class="plan-speed">Up to 2Mb upload</p>
    <div class="plan-price"><span class="price-currency">$</span><span class="price-whole">74</span><span class="price-cents">.99</span></div>
    <p class="plan-fee">+ $100 install fee</p>
    <a class="buy-button" href="#">Buy Now</a>
  </article>
</body>
</html>
```